This book will apply the 12 Steps to gaming addiction, also known as video game addiction. The primary purpose of the book is to provide an effective solution for this new type of addiction. The solution is based on the rich and successful concepts of traditional twelve-step programs like RL.

The title on the cover will be "Nine Doors Past the Glowing Screen" and "by Martin Quorby". A subtitle can be used if it works in your design of "A Practical Path Beyond Compulsive Console Play". Cover will be for a 6" x 9" book approximately 110 pages in length.

Some back cover text including some review quotes and an author bio are in the attached Word doc. There is also an author photo attached for for the back cover.

Requirements
Must have
• For the cover design it could be stylized, or an image, a partial image, or whatever. I am open to suggestions. Think about what would be noticed by a person searching for help with moderating their video game use, or by the parents or loved ones of problem gamers. Something contemporary and eye catching.

```html
<!DOCTYPE html>
<html lang="en">
<head>
<meta charset="utf-8">
<title>Nine Doors Past the Glowing Screen — Martin Quorby</title>
<link rel="stylesheet" href="https://fonts.googleapis.com/css2?family=Montserrat:wght@400;500;700&family=Nunito+Sans:wght@700;800;900&display=swap">
<style>
  :root {
    --page-bg: #f5f5f5;
    --cover-dark: #15111f;
    --cover-navy: #1c1630;
    --photo-pink: #e0529a;
    --photo-green: #6ee07a;
    --photo-purple: #5a2f6e;
    --neon-green: #3dff6e;
    --rule-yellow: #f3f20c;
    --title-red: #f55a5a;
    --author-green: #5fd160;
    --text-white: #ffffff;
  }
  * { margin: 0; padding: 0; box-sizing: border-box; }
  html, body { width: 1200px; height: 1200px; overflow: hidden; background: var(--page-bg); }
  .stage { position: relative; width: 1200px; height: 1200px; }
  .cover {
    position: absolute; left: 267px; top: 100px; width: 667px; height: 1000px;
    overflow: hidden; background: var(--cover-dark);
  }
  .cover-photo {
    position: absolute; inset: 0;
    background:
      radial-gradient(ellipse 38% 26% at 30% 10%, rgba(235,110,170,.95), transparent 70%),
      radial-gradient(ellipse 30% 28% at 68% 12%, rgba(120,230,120,.9), transparent 70%),
      radial-gradient(ellipse 28% 22% at 82% 45%, rgba(70,120,80,.75), transparent 70%),
      radial-gradient(ellipse 70% 30% at 45% 48%, rgba(110,55,130,.9), transparent 75%),
      linear-gradient(180deg, #3a1a3a 0%, #3d2450 38%, #2a1d3e 60%, var(--cover-navy) 80%, var(--cover-dark) 100%);
  }
  .title-block { position: absolute; inset: 0; text-align: center; color: var(--text-white); }
  .title-neon {
    position: absolute; left: 0; right: 0; top: 468px;
    font-family: "Montserrat", sans-serif; font-weight: 700; font-size: 88px; line-height: 1;
    letter-spacing: 1px; color: transparent;
    -webkit-text-stroke: 3px var(--neon-green);
    text-shadow: 0 0 10px rgba(61,255,110,.65), 0 0 22px rgba(61,255,110,.35);
  }
  .title-link {
    position: absolute; left: 68px; right: 68px; top: 600px; height: 30px;
    display: flex; align-items: center; gap: 12px;
    font-family: "Montserrat", sans-serif; font-weight: 500; font-size: 26px;
  }
  .title-link::before, .title-link::after {
    content: ""; flex: 1; height: 5px; border-radius: 3px;
    background: linear-gradient(90deg, rgba(243,242,12,.35), var(--rule-yellow) 40%, var(--rule-yellow) 60%, rgba(243,242,12,.35));
  }
  .title-main {
    position: absolute; left: 0; right: 0; top: 648px;
    font-family: "Nunito Sans", sans-serif; font-weight: 800; font-size: 66px; line-height: 1.1;
    color: var(--title-red); letter-spacing: 1px;
  }
  .subtitle {
    position: absolute; left: 0; right: 0; top: 818px;
    font-family: "Montserrat", sans-serif; font-weight: 500; font-size: 25px; line-height: 1.35;
    letter-spacing: 2px; text-transform: uppercase;
  }
  .author {
    position: absolute; left: 0; right: 0; top: 918px;
    font-family: "Nunito Sans", sans-serif; font-weight: 900; font-size: 48px; line-height: 1;
    letter-spacing: 3px; color: var(--author-green); text-transform: uppercase;
  }
</style>
</head>
<body>
  <main class="stage">
    <section class="cover">
      <div class="cover-photo" role="img" aria-label="Blurred close-up of a young gamer holding a game controller, lit by pink and green neon light"></div>
      <div class="title-block">
        <h1>
          <span class="title-neon">NINE DOORS</span>
          <span class="title-link">PAST THE</span>
          <span class="title-main">GLOWING<br>SCREEN</span>
        </h1>
        <p class="subtitle">A Practical Path Beyond<br>Compulsive Console Play</p>
        <p class="author">Martin Quorby</p>
      </div>
    </section>
  </main>
</body>
</html>
```